Commercial Construction Interior Fitout company needs Logo and Business Cards

We need a logo and business card design. We specialise in Commercial Ceilings, Partitions, Plastering and Carpentry.

Company name: 7QX Commercial Interiors. Would like a professional looking card more than a fancy look. Gloss front preferably black pattern with Fluro Green and white text.

Will need:

Name
Position
Phone
Fax
Email
Postal Address
Web address
Updates

Thank you so much everyone for your efforts and fantastic designs..   If I didn't respond to everyone personally,  my apologises. 

Again, thanks all

R.M                               

Target Market(s)

Existing & New clients in the Construction Industry

Industry/Entity Type

Business

Requirements
Nice to have
• 7QX to be overlapped or made into some sort of Logo

```html
<!DOCTYPE html>
<html lang="en">
<head>
<meta charset="utf-8">
<title>7QX Commercial Interiors – Business Card</title>
<link rel="stylesheet" href="https://fonts.googleapis.com/css2?family=Michroma&family=Open+Sans:wght@400;600&display=swap">
<style>
  :root {
    --card-black: #1c1b1a;
    --fluro-green: #b5d43b;
    --card-white: #ffffff;
    --text-light: #e9e9e6;
    --backdrop: #d9d6d1;
  }
  * { box-sizing: border-box; margin: 0; padding: 0; }
  html, body {
    width: 1200px;
    height: 640px;
    overflow: hidden;
    background: var(--backdrop);
  }
  .canvas {
    position: relative;
    width: 1200px;
    height: 640px;
  }
  .card {
    position: absolute;
    top: 160px;
    width: 540px;
    height: 320px;
    background: var(--card-black);
    box-shadow: 0 4px 14px rgba(0,0,0,0.25);
  }
  .card-front { left: 40px; }
  .card-back  { left: 620px; }

  /* Front */
  .brand {
    position: absolute;
    left: 0; right: 0;
    top: 118px;
    display: flex;
    align-items: center;
    justify-content: center;
    gap: 14px;
  }
  .brand-square {
    width: 22px;
    height: 22px;
    background: var(--fluro-green);
  }
  .brand-name {
    font-family: "Michroma", sans-serif;
    font-size: 20px;
    color: var(--card-white);
    letter-spacing: 1px;
  }
  .front-web {
    position: absolute;
    left: 0; right: 0;
    top: 200px;
    text-align: center;
    font-family: "Open Sans", sans-serif;
    font-size: 15px;
    letter-spacing: 1.5px;
    color: var(--text-light);
  }

  /* Back */
  .stripe {
    position: absolute;
    left: 0;
    width: 100%;
    height: 5px;
    background: var(--fluro-green);
  }
  .stripe-top-1 { top: 26px; }
  .stripe-top-2 { top: 40px; }
  .stripe-bottom-1 { top: 274px; }
  .stripe-bottom-2 { top: 288px; }

  .name-frame {
    position: absolute;
    left: 59px;
    top: 106px;
    width: 148px;
    height: 112px;
    border: 6px solid var(--fluro-green);
    border-radius: 9px;
  }
  .name-block {
    position: absolute;
    left: 38px;
    top: 143px;
    width: 190px;
    text-align: center;
  }
  .person-name {
    display: inline-block;
    background: var(--card-black);
    padding: 0 4px;
    font-family: "Michroma", sans-serif;
    font-size: 15px;
    color: var(--card-white);
    letter-spacing: 1px;
    line-height: 20px;
  }
  .person-role {
    display: inline-block;
    margin-top: 3px;
    background: var(--card-black);
    padding: 0 4px;
    font-family: "Open Sans", sans-serif;
    font-size: 11px;
    color: var(--card-white);
    letter-spacing: 4px;
  }

  .contact {
    position: absolute;
    left: 291px;
    top: 104px;
    font-family: "Open Sans", sans-serif;
    font-size: 14px;
    line-height: 19px;
    color: var(--text-light);
  }
  .address { margin-bottom: 14px; }
  .contact-row { display: flex; }
  .contact-label { width: 58px; }
  .contact-web {
    margin-top: 12px;
    letter-spacing: 1px;
  }
</style>
</head>
<body>
<main class="canvas">
  <section class="card card-front" aria-label="Card front">
    <div class="brand">
      <span class="brand-square"></span>
      <span class="brand-name">7QX Commercial Interiors</span>
    </div>
    <p class="front-web">www.7qx.com</p>
  </section>

  <section class="card card-back" aria-label="Card back">
    <div class="stripe stripe-top-1"></div>
    <div class="stripe stripe-top-2"></div>

    <div class="name-frame"></div>
    <div class="name-block">
      <span class="person-name">DANE HOLLIS</span><br>
      <span class="person-role">MANAGER</span>
    </div>

    <div class="contact">
      <p class="address">Millbrook 412<br>Eastvale</p>
      <p class="contact-row"><span class="contact-label">phone</span><span>62 48115037</span></p>
      <p class="contact-row"><span class="contact-label">fax</span><span>982 5530194</span></p>
      <p class="contact-row"><span class="contact-label">email</span><span>DH@7qx.com</span></p>
      <p class="contact-web">www.7qx.com</p>
    </div>

    <div class="stripe stripe-bottom-1"></div>
    <div class="stripe stripe-bottom-2"></div>
  </section>
</main>
</body>
</html>
```